Edgy rebranded biz cards KRB

We are rebranding our 20 yr old mortgage company with a new logo and would like cards to compliment our new look.

Target Market(s)

potential home buyers or clients for refinance

Industry/Entity Type

Mortgage Brokerage

Contact Information for Business Card

418 W. Lomita Ave #305
Henderson, NV 89152
702.519.4827 o
702-519-4829 f
www.kestrelridgelending,example
nmls 842019
KRB is an equal housing lender

Font styles to use
Sans Serif

Colors
0455a3
3176b5
0393ce
33a6d7

Requirements
Must have
• space for a photo
Nice to have
• One side with the company info and the other with the person's info

```html
<!DOCTYPE html>
<html lang="en">
<head>
<meta charset="utf-8">
<title>Kestrel Ridge Lending – Business Cards</title>
<link href="https://fonts.googleapis.com/css2?family=Montserrat:wght@400;500;700;800&family=Oswald:wght@600&display=swap" rel="stylesheet">
<style>
  :root {
    --bg: #4a4a4a;
    --paper: #ffffff;
    --brand-blue: #0570bf;
    --brand-deep: #0455a3;
    --ink: #3a3a3a;
    --muted: #6b6b6b;
    --faint: #e6eff8;
    --photo-dark: #2b2b2b;
    --photo-mid: #3a3a3a;
  }
  * { box-sizing: border-box; margin: 0; padding: 0; }
  html, body { width: 1200px; height: 800px; overflow: hidden; }
  body {
    background: var(--bg);
    font-family: "Montserrat", sans-serif;
    position: relative;
  }
  .card {
    position: absolute;
    overflow: hidden;
    box-shadow: 0 12px 30px rgba(0,0,0,.35);
  }

  /* Front: personal info */
  .card-front {
    left: 110px; top: 70px;
    width: 380px; height: 660px;
    background: var(--paper);
    border-bottom: 4px solid var(--brand-blue);
  }
  .front-mark {
    position: absolute;
    left: -20px; bottom: -30px;
    font-family: "Montserrat", sans-serif;
    font-weight: 800;
    font-size: 210px;
    letter-spacing: -6px;
    color: var(--faint);
    line-height: 1;
  }
  .front-content {
    position: absolute;
    top: 120px; left: 0; right: 0;
    text-align: center;
  }
  .brand-lockup { display: inline-block; }
  .brand-initials {
    font-weight: 800;
    font-size: 64px;
    color: var(--brand-blue);
    letter-spacing: 2px;
    line-height: 1;
  }
  .brand-name {
    margin-top: 10px;
    font-weight: 800;
    font-size: 22px;
    color: var(--brand-blue);
    letter-spacing: 1px;
    padding-bottom: 8px;
    border-bottom: 2px solid #8a8a8a;
  }
  .brand-sub {
    margin-top: 6px;
    font-size: 13px;
    letter-spacing: 3px;
    color: var(--muted);
  }
  .person-name {
    margin-top: 36px;
    font-family: "Oswald", sans-serif;
    font-weight: 600;
    font-size: 30px;
    color: var(--brand-blue);
    letter-spacing: 1px;
  }
  .person-title { font-size: 14px; color: var(--muted); letter-spacing: 1px; }
  .dots {
    margin: 14px auto;
    width: 60px;
    border-top: 2px dotted var(--ink);
  }
  .contact { font-size: 14px; line-height: 1.55; color: var(--ink); }
  .contact + .contact { margin-top: 14px; }

  /* Back: company side */
  .card-back {
    left: 540px; top: 225px;
    width: 600px; height: 350px;
    background: var(--brand-blue);
    border-left: 3px solid var(--brand-deep);
  }
  .photo-area {
    position: absolute;
    left: 20px; bottom: 0;
    width: 270px; height: 280px;
    border-radius: 120px 120px 0 0;
    background: linear-gradient(180deg, var(--photo-mid), var(--photo-dark));
  }
  .back-brand {
    position: absolute;
    right: 40px; bottom: 70px;
    text-align: right;
    color: var(--paper);
  }
  .back-initials {
    font-weight: 800;
    font-size: 96px;
    letter-spacing: 2px;
    line-height: 1;
  }
  .back-tagline {
    margin-top: 6px;
    font-weight: 500;
    font-size: 15px;
  }
</style>
</head>
<body>

  <section class="card card-front" aria-label="Business card front">
    <div class="front-mark" aria-hidden="true">KRB</div>
    <div class="front-content">
      <div class="brand-lockup">
        <div class="brand-initials">KRB</div>
        <div class="brand-name">KESTREL RIDGE</div>
        <div class="brand-sub">LENDING</div>
      </div>
      <div class="person-name">DANIEL REYES</div>
      <div class="person-title">President</div>
      <div class="dots"></div>
      <p class="contact">418 W. Lomita Ave #305<br>Henderson, NV 89152</p>
      <p class="contact">Tel. 702.519.4827<br>Cell. 702-519-4829<br>www.kestrelridgelending.example</p>
      <div class="dots"></div>
      <p class="contact">NMLS : 842019</p>
    </div>
  </section>

  <section class="card card-back" aria-label="Business card back">
    <div class="photo-area" role="img" aria-label="Portrait photo of the president in suit and tie"></div>
    <div class="back-brand">
      <div class="back-initials">KRB</div>
      <div class="back-tagline">KRB is an Equal Housing Lender</div>
    </div>
  </section>

</body>
</html>
```